Obrelo Business Card

Need a double sided business card. Would like the business card to have the logo on one side and the employees details and business contact details on the other.

Business

```html
<!DOCTYPE html>
<html lang="en">
<head>
<meta charset="utf-8">
<title>Obrelo Business Card</title>
<link rel="stylesheet" href="https://fonts.googleapis.com/css2?family=Arimo:wght@400;700&family=Tinos&family=Cinzel:wght@400&display=swap">
<style>
  :root {
    --lime: #a3cb4a;
    --ink: #050505;
    --steel: #8a8f93;
    --paper: #ffffff;
    --faint: #1c1d1e;
    --backdrop: #e9e7e3;
    --name-ink: #2a2a2a;
  }
  * { margin: 0; padding: 0; box-sizing: border-box; }
  html, body { width: 1200px; height: 813px; overflow: hidden; }
  body { background: var(--backdrop); position: relative; font-family: "Arimo", Arial, sans-serif; }

  .card {
    position: absolute;
    width: 540px;
    height: 300px;
    overflow: hidden;
    box-shadow: 0 8px 22px rgba(0,0,0,0.25);
  }
  .card--front { left: 330px; top: 60px; background: var(--lime); }
  .card--back-light { left: 50px; top: 440px; background: var(--lime); }
  .card--back-dark { left: 610px; top: 440px; background: var(--ink); }

  .card__shape { position: absolute; inset: 0; width: 100%; height: 100%; }

  .wordmark {
    position: absolute;
    font-family: "Arimo", Arial, sans-serif;
    font-weight: 700;
    letter-spacing: 1px;
    line-height: 1;
  }
  .wordmark__dot {
    display: inline-block;
    vertical-align: top;
    margin-left: 8px;
  }

  .card--front .wordmark { left: 34px; top: 82px; font-size: 64px; color: var(--lime); }
  .card--front .wordmark__dot { width: 14px; height: 14px; background: var(--lime); }

  .holder {
    position: absolute;
    right: 42px;
    top: 22px;
    text-align: right;
    font-family: "Cinzel", Georgia, serif;
    color: var(--name-ink);
    line-height: 1.05;
  }
  .holder__name { font-size: 19px; }
  .holder__title { font-size: 15px; }

  .contact {
    position: absolute;
    left: 50px;
    top: 200px;
    font-family: "Tinos", "Times New Roman", serif;
    color: var(--paper);
    font-size: 15px;
    line-height: 1.25;
    list-style: none;
  }
  .contact__address { margin-top: 8px; }

  .faint-square {
    position: absolute;
    border-radius: 10px;
    background: var(--faint);
  }
  .card--front .faint-square { left: 300px; top: 135px; width: 150px; height: 130px; }

  .card--back-light .wordmark { left: 0; right: 0; top: 96px; text-align: center; font-size: 92px; color: var(--paper); }
  .card--back-light .wordmark__dot { width: 20px; height: 20px; background: var(--paper); }
  .card--back-light .site { color: var(--ink); }

  .card--back-dark .faint-square { left: 170px; top: 40px; width: 220px; height: 220px; }
  .card--back-dark .wordmark { left: 0; right: 0; top: 82px; text-align: center; font-size: 82px; color: var(--lime); }
  .card--back-dark .wordmark__dot { width: 18px; height: 18px; background: var(--lime); }
  .card--back-dark .site { color: var(--paper); }

  .site {
    position: absolute;
    left: 0; right: 0;
    bottom: 58px;
    text-align: center;
    font-size: 17px;
    letter-spacing: 1.5px;
  }
</style>
</head>
<body>

  <section class="card card--front" aria-label="Business card front">
    <svg class="card__shape" viewBox="0 0 540 300" preserveAspectRatio="none" aria-hidden="true">
      <path d="M0 36 Q330 -10 524 300 L0 300 Z" fill="var(--ink)"/>
      <path d="M0 32 Q338 -18 532 270" fill="none" stroke="var(--steel)" stroke-width="6"/>
    </svg>
    <div class="faint-square"></div>
    <div class="holder">
      <p class="holder__name">Your Name</p>
      <p class="holder__title">Title</p>
    </div>
    <div class="wordmark">obrelo<span class="wordmark__dot"></span></div>
    <ul class="contact">
      <li>P: 555-210-4830</li>
      <li>F: 555-210-4831</li>
      <li>E: hello@obrelo.com</li>
      <li class="contact__address">Street Name City Name</li>
      <li>State ZipCode</li>
    </ul>
  </section>

  <section class="card card--back-light" aria-label="Business card back, light">
    <div class="wordmark">obrelo<span class="wordmark__dot"></span></div>
    <p class="site">www.obrelo.com</p>
  </section>

  <section class="card card--back-dark" aria-label="Business card back, dark">
    <div class="faint-square"></div>
    <div class="wordmark">obrelo<span class="wordmark__dot"></span></div>
    <p class="site">www.obrelo.com</p>
  </section>

</body>
</html>
```